Fundrally Slides

I need a graphic designer go through the attached power point presentation (4 slides) and make it look clean, modern, and branded.

The four slides are currently displayed as jpegs on the Fundrally viewing page below -
Here is the Fundrally preview link:: https://www.fundrally.example/projects/4826153907/5390284716?token=3c7a91f2
Updates

Project Deadline Extended

Industry/Entity Type

Graphic Designer

Requirements
Must have
• Simple, clean same color scheme as logo

```html
<!DOCTYPE html>
<html lang="en">
<head>
<meta charset="utf-8">
<title>The Business – Page 4</title>
<link href="https://fonts.googleapis.com/css2?family=Pathway+Gothic+One&family=Roboto+Condensed:ital,wght@0,400;0,700;1,700&family=Open+Sans:wght@700&display=swap" rel="stylesheet">
<style>
  :root {
    --ink: #1b1b1b;
    --accent: #3e6fa8;
    --accent-dark: #1d4f8f;
    --band: #1e78c8;
    --band-dark: #0d4f92;
    --tab-dark: #141414;
    --card-line: #9a9a9a;
    --page: #ffffff;
    --muted: #4a6a96;
  }
  * { box-sizing: border-box; margin: 0; padding: 0; }
  html, body { width: 1200px; height: 1000px; overflow: hidden; background: var(--page); }
  body { position: relative; font-family: "Roboto Condensed", sans-serif; color: var(--ink); }

  .slide {
    position: absolute; left: 92px; top: 103px; width: 1018px; height: 765px;
    border: 1.5px solid var(--card-line); border-radius: 30px; background: var(--page);
    box-shadow: 8px 10px 6px rgba(0,0,0,0.35);
  }

  .title-tabs { position: absolute; left: 6px; top: 17px; display: flex; gap: 2px; }
  .title-tabs span {
    display: block; height: 52px; line-height: 52px; padding-left: 10px;
    font-family: "Pathway Gothic One", sans-serif; font-size: 34px; color: #fff;
    border: 2px solid #555;
  }
  .tab-the { width: 104px; background: linear-gradient(#4d7fc0, var(--accent-dark)); }
  .tab-business { width: 180px; background: var(--tab-dark); }

  .brand { position: absolute; right: 40px; top: 34px; display: flex; align-items: center; gap: 8px; }
  .brand-mark { width: 14px; height: 14px; background: var(--accent-dark); }
  .brand-name { font-family: "Roboto Condensed", sans-serif; font-weight: 700; font-size: 30px; color: var(--tab-dark); }

  .section-title {
    position: absolute; left: 10px; font-family: "Pathway Gothic One", sans-serif;
    font-size: 26px; color: var(--accent);
  }
  .body-text { position: absolute; left: 10px; width: 1000px; font-size: 18.5px; line-height: 27px; letter-spacing: -0.2px; }
  .body-text em { font-weight: 700; font-style: italic; }

  .duties { position: absolute; left: 10px; top: 320px; width: 1000px; list-style: none; font-size: 15.5px; line-height: 24px; letter-spacing: -0.3px; }
  .duties li::before { content: "➢"; font-weight: 700; margin-right: 2px; }
  .duties strong { font-size: 19px; }

  .callout {
    position: absolute; left: -2px; top: 481px; width: 596px; height: 39px;
    background: linear-gradient(var(--band), var(--band-dark)); border: 2px solid #445;
    color: #fff; font-family: "Pathway Gothic One", sans-serif; font-size: 22px;
    line-height: 35px; padding-left: 10px;
  }

  .cost-intro { position: absolute; left: 2px; top: 533px; width: 640px; font-size: 16px; line-height: 24px; letter-spacing: -0.3px; }
  .cost-intro strong { color: var(--accent-dark); font-size: 17px; }
  .cost-list { position: absolute; left: 22px; top: 580px; list-style: none; font-size: 16px; line-height: 24px; }
  .cost-list li::before { content: "➢"; }

  .seal { position: absolute; left: 635px; top: 612px; width: 140px; height: 140px; }
  .agency-badge { position: absolute; left: 780px; top: 622px; width: 210px; height: 125px; }

  .footer { position: absolute; left: 40px; top: 733px; font-family: "Open Sans", sans-serif; font-weight: 700; font-size: 13.5px; color: var(--muted); letter-spacing: -0.2px; word-spacing: 2px; }

  .page-label { position: absolute; left: 0; width: 1218px; top: 928px; text-align: center; font-family: "Open Sans", sans-serif; font-weight: 700; font-size: 32px; color: #000; }
</style>
</head>
<body>
  <section class="slide">
    <div class="title-tabs"><span class="tab-the">The</span><span class="tab-business">Business</span></div>
    <div class="brand"><span class="brand-mark"></span><span class="brand-name">SLX</span></div>

    <h2 class="section-title" style="top:84px">Demand &amp; Necessity</h2>
    <p class="body-text" style="top:120px">November 6, 2000 <em>The Needlestick Safety and Prevention Act</em> was passed to reduce injuries and prevent the transmission of bloodborn pathogens that result in viruses and disease.</p>

    <h2 class="section-title" style="top:187px">The law requires employers</h2>
    <p class="body-text" style="top:217px">To use work practice controls and safer devices that are engineered to eliminate or minimize exposure to bloodborne pathogens resulting from needlestick/sharp injuries.</p>

    <h2 class="section-title" style="top:283px">Employers must:</h2>
    <ul class="duties">
      <li><strong>Demonstrate</strong> that they are reviewing new technology that can reduce risk of exposure to bloodborne pathogens by updating exposure control plans and documenting the decision-making process on implementing such technology.</li>
      <li><strong>Maintain</strong> a sharps injury log to track the type and brand of device used, the department or area where the incident occurred, and an explanation of the incident. The log must be maintained in a manner to protect the confidentiality of the injured employee.</li>
      <li><strong style="font-size:16px">Solicit</strong> input from employees responsible for direct patient care in the identification, evaluation and selection of effective safety devices and work practice controls, as part of the ongoing exposure control plan development process. Efforts to encourage staff input must be documented in the plan.</li>
    </ul>

    <div class="callout">This means that when the SLX is available it must be used</div>

    <p class="cost-intro"><strong>The cost of a sharps injury</strong> can be a compelling reason to use safer sharps practices. One sharps injury can cause a number of direct and indirect costs for the health care facility, including:</p>
    <ul class="cost-list">
      <li>Loss of employee time</li>
      <li>Cost of tying up staff to investigate the injury</li>
      <li>Expense of laboratory testing</li>
      <li>Cost of treatment for infected staff</li>
      <li>Cost of replacing staff</li>
    </ul>

    <svg class="seal" viewBox="0 0 140 140" role="img" aria-label="Government seal badge">
      <circle cx="70" cy="70" r="67" fill="#1f2f5c" stroke="#b08a3a" stroke-width="5"/>
      <circle cx="70" cy="70" r="44" fill="#f2efe6"/>
    </svg>
    <svg class="agency-badge" viewBox="0 0 210 125" role="img" aria-label="Safety agency badge">
      <ellipse cx="105" cy="62" rx="102" ry="59" fill="#e6e6e6" stroke="#8a8a8a" stroke-width="4"/>
      <ellipse cx="105" cy="62" rx="88" ry="47" fill="#ffffff"/>
    </svg>

    <p class="footer">Corvane Medical, LLC &nbsp;| &nbsp;1250 Harbor Ave Suite 410 Coral Bay FL 33010 &nbsp;| &nbsp;305. 555.0142</p>
  </section>

  <p class="page-label">Page 4</p>
</body>
</html>
```